Redesign my business cards

I would like pretty much all the same information as my current business cards but redesigned to stand out more and be more unique photo uploaded to show my current business cards don’t mind if you want to remove or replace I for on the back

```html
<!DOCTYPE html>
<html lang="en">
<head>
<meta charset="utf-8">
<title>Halvern Detailing – Business Cards</title>
<link rel="stylesheet" href="https://fonts.googleapis.com/css2?family=Open+Sans:wght@400;600;700;800&display=swap">
<style>
  :root {
    --stage: #232323;
    --card: #12283a;
    --card-deep: #0d1f2e;
    --edge: #22b0f0;
    --edge-glow: rgba(34, 176, 240, .35);
    --accent: #1ea6e6;
    --accent-light: #3cc6f5;
    --accent-deep: #0a78c0;
    --text: #ffffff;
    --muted: #c9dbe8;
    --rule: rgba(30, 166, 230, .35);
  }
  * { box-sizing: border-box; margin: 0; padding: 0; }
  html, body { width: 1200px; height: 780px; overflow: hidden; background: var(--stage); }
  body { font-family: "Open Sans", Arial, sans-serif; color: var(--text); }

  .stage { position: relative; width: 1200px; height: 780px; }

  .card {
    position: absolute;
    top: 70px;
    width: 366px;
    height: 640px;
    background: linear-gradient(165deg, var(--card) 0%, var(--card) 60%, var(--card-deep) 100%);
    border-radius: 26px;
    box-shadow:
      0 0 0 3px var(--edge),
      0 0 22px 2px var(--edge-glow),
      0 20px 44px rgba(0, 0, 0, .6);
    overflow: hidden;
  }
  .card--back { left: 210px; }
  .card--front { left: 624px; }

  /* ---------- Back: service menu ---------- */
  .services {
    padding: 46px 30px 0;
    text-align: center;
  }
  .service { padding: 18px 0; }
  .service + .service { border-top: 1px solid var(--rule); }
  .service__title {
    font-weight: 800;
    font-size: 19px;
    line-height: 1.2;
    color: var(--accent);
    text-transform: uppercase;
    letter-spacing: .2px;
  }
  .service__price {
    display: inline-block;
    margin-top: 6px;
    padding: 2px 12px;
    border-radius: 12px;
    background: var(--accent);
    color: var(--card-deep);
    font-size: 15px;
    font-weight: 800;
  }
  .service__details {
    margin-top: 9px;
    font-size: 13.5px;
    line-height: 1.45;
    color: var(--text);
  }
  .back-brand {
    position: absolute;
    left: 0; right: 0; bottom: 40px;
    display: flex; align-items: center; justify-content: center; gap: 10px;
  }
  .back-brand__dot { width: 14px; height: 14px; border-radius: 50%; background: var(--accent); }
  .back-brand__name { font-weight: 700; font-size: 14px; letter-spacing: 3px; color: var(--accent); }

  /* ---------- Front ---------- */
  .brand {
    position: absolute; top: 84px; left: 0; right: 0;
    display: flex; flex-direction: column; align-items: center; gap: 18px;
  }
  .brand__mark {
    width: 104px; height: 104px; border-radius: 50%;
    background: var(--accent);
    box-shadow: 0 0 30px 6px var(--edge-glow);
  }
  .brand__name { font-weight: 700; font-size: 21px; letter-spacing: 4px; color: var(--accent); }

  .owner { position: absolute; left: 0; right: 0; top: 386px; text-align: center; }
  .owner__name { font-weight: 800; font-size: 34px; line-height: 1.1; color: var(--accent); letter-spacing: .3px; }
  .owner__role { font-weight: 600; font-size: 19px; color: var(--text); margin-top: 2px; }

  .contact-rule { position: absolute; left: 0; top: 470px; width: 366px; height: 40px; }

  .contact { position: absolute; left: 0; right: 0; top: 520px; text-align: center; }
  .contact__phone { font-weight: 700; font-size: 25px; letter-spacing: .8px; }
  .contact__email { font-weight: 600; font-size: 14px; letter-spacing: .4px; margin-top: 4px; color: var(--muted); }
</style>
</head>
<body>
<main class="stage">

  <section class="card card--back" aria-label="Card back – service menu">
    <div class="services">
      <article class="service">
        <h2 class="service__title">Full Extreme Detail</h2>
        <span class="service__price">$350</span>
        <p class="service__details">extreme wash &amp; polish, tyre dressing, engine bay cleaned, vacume &amp; deep clean of carpets &amp; upholstery or leather treatment, interior &amp; exterior trim reviver &amp; protector, window polish and treatment</p>
      </article>
      <article class="service">
        <h2 class="service__title">Exterior Detail</h2>
        <span class="service__price">$250</span>
        <p class="service__details">extreme wash &amp; polish, exterior trim reviver &amp; protector, window polish &amp; treatment, tyre dressing, engine bay cleaned</p>
      </article>
      <article class="service">
        <h2 class="service__title">Interior Detail</h2>
        <span class="service__price">$150</span>
        <p class="service__details">vacume &amp; deep clean of carpets &amp; upholstery or leather treatment, steam clean and stain removal, window polish and treatment, interior trim clean &amp; condition</p>
      </article>
    </div>
    <div class="back-brand">
      <span class="back-brand__dot"></span>
      <span class="back-brand__name">HALVERN DETAILING</span>
    </div>
  </section>

  <section class="card card--front" aria-label="Card front – contact details">
    <div class="brand">
      <span class="brand__mark"></span>
      <span class="brand__name">HALVERN DETAILING</span>
    </div>

    <div class="owner">
      <h1 class="owner__name">OWEN MARLOW</h1>
      <p class="owner__role">owner/operator</p>
    </div>

    <svg class="contact-rule" viewBox="0 0 366 40" aria-hidden="true">
      <g>
        <circle cx="20" cy="20" r="3" fill="#3cc6f5"/>
        <circle cx="36" cy="20" r="4" fill="#33bdf2"/>
        <circle cx="54" cy="20" r="5" fill="#2ab2ee"/>
        <circle cx="74" cy="20" r="6.5" fill="#1ea6e6"/>
        <circle cx="96" cy="20" r="8" fill="#1595d8"/>
        <circle cx="120" cy="20" r="9" fill="#0d86cc"/>
        <circle cx="246" cy="20" r="9" fill="#3cc6f5"/>
        <circle cx="270" cy="20" r="8" fill="#33bdf2"/>
        <circle cx="292" cy="20" r="6.5" fill="#2ab2ee"/>
        <circle cx="312" cy="20" r="5" fill="#1ea6e6"/>
        <circle cx="330" cy="20" r="4" fill="#1595d8"/>
        <circle cx="346" cy="20" r="3" fill="#0d86cc"/>
      </g>
      <g class="icon-phone">
        <circle cx="158" cy="20" r="14" fill="#0a78c0"/>
        <path d="M152 13.5c1-.6 2-.4 2.6.5l1.4 2.2c.5.8.3 1.7-.4 2.3l-1 .8c.9 1.9 2.3 3.4 4.2 4.3l.8-1c.6-.7 1.5-.9 2.3-.4l2.2 1.4c.9.6 1.1 1.6.5 2.6-.8 1.2-2.2 1.9-3.6 1.6-5-1.1-8.9-5-10-10-.3-1.5.4-2.9 1.6-3.7z" fill="#fff"/>
      </g>
      <g class="icon-mail">
        <circle cx="208" cy="20" r="14" fill="#1ea6e6"/>
        <rect x="199" y="13.5" width="18" height="13" rx="1.5" fill="#fff"/>
        <path d="M199.5 14.5l8.5 6.5 8.5-6.5" fill="none" stroke="#1ea6e6" stroke-width="1.6"/>
      </g>
    </svg>

    <div class="contact">
      <p class="contact__phone">0400555271</p>
      <p class="contact__email">HALVERNDETAILING@MAILBOX.COM</p>
    </div>
  </section>

</main>
</body>
</html>
```